Disposable Mini Sauce Pot Design for Asian Chain Food Brands

We operate a Hainan Chicken Rice takeout brand under the name Wokly8, with our official website: www.Wokly8.com.
We offer four signature house sauces and are launching brand-new packaging for our sauce line. We require custom graphic designs exclusively for the sauce cup lids.
Product Material & Base Specs
The sauce cups are made of PP plastic, available in two translucent base options: Translucent White and Translucent Orange.
Four Sauce Varieties for Individual Lid Designs
1. Red Sauce – Fried Sweet Chili Sauce
2.Green Sauce – Scallion Oil Dressing
3.Sweet Soy Sauce
4.Sweet Red Sauce (Special for Fried Chicken)
Differentiate each sauce lid design through unique graphics, typography, or illustrative elements for easy customer identification.
The marking NET WT 2 OZ must be clearly printed on every lid.
**There is no need to print full descriptive text or the full name of the sauces on each lid; the design only needs to clearly differentiate the four sauce varieties.
**Please reference the original design style and brand color palette shown on our official website, and feel free to fully unleash your creativity.
Look and feel
Each slider illustrates characteristics of the customer's brand and the style your logo design should communicate.

```html
<!DOCTYPE html>
<html lang="en">
<head>
<meta charset="utf-8">
<title>Wokly8 Sauce Lids</title>
<link href="https://fonts.googleapis.com/css2?family=Oswald:wght@500;700&family=Roboto+Condensed:wght@500;700&family=Nunito:wght@800&display=swap" rel="stylesheet">
<style>
  :root {
    --page: #ececec;
    --cream: #fbf4df;
    --white: #ffffff;

    --chili-top: #f07d1c;
    --chili-bottom: #c4221c;
    --chili-stroke: #7e1210;
    --chili-tab: #ea6a1d;
    --chili-art: rgba(214, 58, 24, 0.55);
    --chili-art-2: rgba(246, 176, 40, 0.6);

    --green-top: #d6eaa9;
    --green-bottom: #2c8540;
    --green-ink: #2c682b;
    --green-stroke: #245f26;
    --green-fill: #f3f1c8;
    --green-tab: #7cc04c;
    --green-art: rgba(120, 190, 90, 0.55);
    --green-art-2: rgba(236, 226, 210, 0.55);

    --soy-top: #120a06;
    --soy-mid: #3a2213;
    --soy-bottom: #0f0805;
    --soy-fill: #f6e7c6;
    --soy-stroke: #2a160a;
    --soy-tab: #4b2c18;
    --soy-art: rgba(140, 96, 58, 0.6);
    --soy-art-2: rgba(92, 20, 14, 0.6);

    --chicken-top: #8c1a30;
    --chicken-bottom: #e9552a;
    --chicken-stroke: #8e1414;
    --chicken-tab: #8c1a30;
    --chicken-art: rgba(222, 130, 50, 0.6);
    --chicken-art-2: rgba(232, 80, 30, 0.55);
  }

  * { box-sizing: border-box; margin: 0; padding: 0; }

  html, body {
    width: 1042px;
    height: 1200px;
    overflow: hidden;
    background: var(--page);
  }

  .lid-sheet {
    width: 1042px;
    height: 1200px;
    display: grid;
    grid-template-columns: repeat(2, 440px);
    grid-template-rows: repeat(2, 510px);
    gap: 50px 40px;
    justify-content: center;
    align-content: center;
  }

  .lid {
    position: relative;
    border-radius: 44px;
    overflow: hidden;
    text-align: center;
    color: var(--white);
  }

  .lid--chili { background: linear-gradient(180deg, var(--chili-top) 0%, #e4491c 45%, var(--chili-bottom) 100%); }
  .lid--green { background: linear-gradient(180deg, var(--green-top) 0%, #79b955 50%, var(--green-bottom) 100%); }
  .lid--soy { background: radial-gradient(ellipse at 50% 60%, var(--soy-mid) 0%, var(--soy-top) 70%, var(--soy-bottom) 100%); }
  .lid--chicken { background: linear-gradient(180deg, var(--chicken-top) 0%, #c0322f 55%, var(--chicken-bottom) 100%); }

  .lid__kicker {
    position: absolute;
    top: 40px;
    left: 0;
    right: 0;
    font-family: "Roboto Condensed", sans-serif;
    font-weight: 700;
    font-size: 27px;
    line-height: 1;
    letter-spacing: 0.3px;
  }

  .lid__subtitle {
    position: absolute;
    top: 72px;
    left: 0;
    right: 0;
    font-family: "Roboto Condensed", sans-serif;
    font-weight: 500;
    font-size: 21px;
    line-height: 1;
  }

  .lid--green .lid__kicker,
  .lid--green .lid__subtitle { color: var(--green-ink); }

  .lid__art {
    position: absolute;
    border-radius: 50%;
    filter: blur(6px);
  }

  .lid__headline {
    position: absolute;
    left: 0;
    right: 0;
    font-family: "Oswald", sans-serif;
    font-weight: 700;
    line-height: 0.95;
    letter-spacing: -0.5px;
    paint-order: stroke fill;
  }

  .lid--chili .lid__headline {
    top: 162px;
    font-size: 92px;
    color: var(--cream);
    -webkit-text-stroke: 10px var(--chili-stroke);
  }
  .lid--green .lid__headline {
    top: 168px;
    font-size: 86px;
    color: var(--green-fill);
    -webkit-text-stroke: 10px var(--green-stroke);
  }
  .lid--soy .lid__headline {
    top: 158px;
    font-size: 96px;
    color: var(--soy-fill);
    -webkit-text-stroke: 8px var(--soy-stroke);
  }
  .lid--chicken .lid__headline {
    top: 196px;
    font-size: 86px;
    color: var(--white);
    -webkit-text-stroke: 10px var(--chicken-stroke);
  }

  .lid__brand {
    position: absolute;
    bottom: 66px;
    left: 0;
    right: 0;
    font-family: "Nunito", sans-serif;
    font-weight: 800;
    font-size: 32px;
    line-height: 1;
    color: var(--cream);
  }

  .lid__weight {
    position: absolute;
    bottom: 40px;
    left: 0;
    right: 0;
    font-family: "Roboto Condensed", sans-serif;
    font-weight: 500;
    font-size: 18px;
    line-height: 1;
    color: var(--cream);
  }

  .lid__tab {
    position: absolute;
    right: 0;
    bottom: 0;
    width: 130px;
    height: 130px;
    clip-path: polygon(100% 0, 100% 100%, 0 100%);
  }
  .lid--chili .lid__tab { background: var(--chili-tab); }
  .lid--green .lid__tab { background: var(--green-tab); }
  .lid--soy .lid__tab { background: var(--soy-tab); }
  .lid--chicken .lid__tab { background: var(--chicken-tab); }

  .lid__tab-label {
    position: absolute;
    right: 30px;
    bottom: 50px;
    transform: rotate(-45deg);
    font-family: "Nunito", sans-serif;
    font-weight: 800;
    font-size: 19px;
    color: var(--cream);
    white-space: nowrap;
  }

  .lid__tab-arrow {
    position: absolute;
    right: 20px;
    bottom: 20px;
    width: 26px;
    height: 26px;
  }
</style>
</head>
<body>
<main class="lid-sheet">

  <!-- Red Sauce -->
  <section class="lid lid--chili">
    <p class="lid__kicker">RED SAUCE</p>
    <p class="lid__subtitle">Fried Sweet Chili Sauce</p>
    <div class="lid__art" role="img" aria-label="Illustration of red chili peppers"
         style="left:40px; top:130px; width:140px; height:300px; background: radial-gradient(circle, var(--chili-art) 0%, transparent 70%);"></div>
    <div class="lid__art" role="img" aria-label="Illustration of a honey jar with dipper and sugar cane"
         style="left:270px; top:100px; width:150px; height:200px; background: radial-gradient(circle, var(--chili-art-2) 0%, transparent 70%);"></div>
    <h2 class="lid__headline">CHILI<br>SWEET</h2>
    <p class="lid__brand">Wokly8</p>
    <p class="lid__weight">NET WT 2 OZ.</p>
    <div class="lid__tab"></div>
    <span class="lid__tab-label">Pull here</span>
    <svg class="lid__tab-arrow" viewBox="0 0 26 26" aria-hidden="true"><polygon points="26,0 26,26 0,26" fill="#ffffff"/></svg>
  </section>

  <!-- Green Sauce -->
  <section class="lid lid--green">
    <p class="lid__kicker">GREEN SAUCE</p>
    <p class="lid__subtitle">Scallion Oil Dressing</p>
    <div class="lid__art" role="img" aria-label="Illustration of chopped scallions"
         style="left:30px; top:120px; width:200px; height:300px; background: radial-gradient(circle, var(--green-art) 0%, transparent 70%);"></div>
    <div class="lid__art" role="img" aria-label="Illustration of spring onion stalks and garlic cloves"
         style="left:230px; top:110px; width:190px; height:290px; background: radial-gradient(circle, var(--green-art-2) 0%, transparent 70%);"></div>
    <h2 class="lid__headline">SCALLION<br>OIL</h2>
    <p class="lid__brand">Wokly8</p>
    <p class="lid__weight">NET WT 2 OZ.</p>
    <div class="lid__tab"></div>
    <span class="lid__tab-label">Pull here</span>
    <svg class="lid__tab-arrow" viewBox="0 0 26 26" aria-hidden="true"><polygon points="26,0 26,26 0,26" fill="#ffffff"/></svg>
  </section>

  <!-- Sweet Soy Sauce -->
  <section class="lid lid--soy">
    <p class="lid__kicker">SWEET SOY SAUCE</p>
    <div class="lid__art" role="img" aria-label="Illustration of a wooden barrel"
         style="left:30px; top:250px; width:110px; height:130px; background: radial-gradient(circle, var(--soy-art) 0%, transparent 70%);"></div>
    <div class="lid__art" role="img" aria-label="Illustration of a wooden barrel"
         style="left:300px; top:250px; width:110px; height:130px; background: radial-gradient(circle, var(--soy-art) 0%, transparent 70%);"></div>
    <div class="lid__art" role="img" aria-label="Illustration of soy sauce splashes and drips"
         style="left:300px; top:100px; width:110px; height:80px; background: radial-gradient(circle, var(--soy-art-2) 0%, transparent 70%);"></div>
    <h2 class="lid__headline">SWEET<br>SOY</h2>
    <p class="lid__brand">Wokly8</p>
    <p class="lid__weight">NET WT 2 OZ.</p>
    <div class="lid__tab"></div>
    <span class="lid__tab-label">Pull here</span>
    <svg class="lid__tab-arrow" viewBox="0 0 26 26" aria-hidden="true"><polygon points="26,0 26,26 0,26" fill="#ffffff"/></svg>
  </section>

  <!-- Sweet Red Sauce -->
  <section class="lid lid--chicken">
    <p class="lid__kicker">SWEET RED SAUCE</p>
    <p class="lid__subtitle">(Fried Chicken)</p>
    <div class="lid__art" role="img" aria-label="Illustration of a fried chicken drumstick drizzled with sauce"
         style="left:70px; top:100px; width:300px; height:130px; background: radial-gradient(ellipse, var(--chicken-art) 0%, transparent 70%);"></div>
    <div class="lid__art" role="img" aria-label="Illustration of sauce dripping over the lettering"
         style="left:60px; top:330px; width:320px; height:70px; background: radial-gradient(ellipse, var(--chicken-art-2) 0%, transparent 70%);"></div>
    <h2 class="lid__headline">SWEET<br>CHICKEN</h2>
    <p class="lid__brand">Wokly8</p>
    <p class="lid__weight">NET WT 2 OZ.</p>
    <div class="lid__tab"></div>
    <span class="lid__tab-label">Pull here</span>
    <svg class="lid__tab-arrow" viewBox="0 0 26 26" aria-hidden="true"><polygon points="26,0 26,26 0,26" fill="#ffffff"/></svg>
  </section>

</main>
</body>
</html>
```